Automotive Mechanic Website Design

We are working with an auto repair shop in California.
A few websites for inspiration:
https://brindlecovemotors.example
https://www.folionest.example/gallery/57316284/Torvane-Auto-Services-Repair-SiteKit-Theme
http://www.quelbrightmotors.example
https://www.halvikgarage.example
https://www.pdmotorhaus.example
Thank you for taking the time to consider designing a website for us. We are web developers based in Stockton, CA, USA. Most of our projects go through the same process. Understanding this process may help you win a project with us. We custom-code all of our websites in-house. We don’t have any requirements as to what tools you use for your design, but we ask that you follow these guidelines.
IMAGES:
If you use any images or icons in the design, we ask that you have a link to the asset so we can purchase the image/icon. Most of the designs we submit do not have the customer’s images on them unless they have some great images. Be creative; show us the feeling you are trying to portray with your image choices. Use any royalty-free site you choose. We subscribe to Adobe and mainly use their images, but we can purchase images outside of Adobe. PLEASE NOTE: we will not submit designs to clients with watermarks on the images.
FONTS:
We ask that you identify the fonts you’re using in the design. This can be done in a message if you want. We typically use Google Fonts and Adobe Fonts.
CONTENT:
We're always open to different content and ideas. We often submit designs with stock images so the client can see our vision. We typically take pictures after the website launch to use their images with our vision. Lorem Ipsum is fine for paragraphs, but we ask that you make the Headers with correct English. We want to be able to show the vision and identify the sections of the website.
INSPIRATION:
We typically add a couple of links in the brief of websites we like to help you get started in your design.
REVISIONS:
We do not often ask for revisions of the designs unless we see something in the design that may not appeal to the client. If there are slight changes that we want to make, we do that in the development process.
FEEDBACK:
We rarely give feedback on designs during the design process. We are working on many website projects and do not have the time to provide feedback. We usually respond if your request is well thought out and asks specific questions, but a note asking “feedback, please” usually goes unanswered.

```html
<!DOCTYPE html>
<html lang="en">
<head>
<meta charset="utf-8">
<title>Veltra Auto Repair</title>
<link href="https://fonts.googleapis.com/css2?family=Barlow:ital,wght@0,400;0,500;0,600;0,700;0,800;1,500;1,700&display=swap" rel="stylesheet">
<style>
:root{
  --red:#F2454A;
  --red-soft:#F7A3A5;
  --ink:#111216;
  --text:#2a2a2e;
  --muted:#55565c;
  --line:#c9c9cc;
  --paper:#ffffff;
  --panel:#EDE9E9;
  --photo-grey:#c9cacd;
}
*{margin:0;padding:0;box-sizing:border-box}
html,body{width:1200px;height:3339px;overflow:hidden;background:var(--paper)}
body{font-family:'Barlow',sans-serif;color:var(--text)}
.canvas{position:relative;width:1200px;height:3339px;overflow:hidden}
.abs{position:absolute}
.shape{position:absolute;left:0;top:0}
.btn{position:absolute;display:flex;align-items:center;justify-content:center;font-weight:700;letter-spacing:1.5px;font-size:13px;color:#fff;background:var(--ink);clip-path:polygon(10% 0,100% 0,90% 100%,0 100%)}
.btn.red{background:var(--red);letter-spacing:0.5px;font-weight:500;font-size:14px}
.kicker{position:absolute;font-size:17px;font-weight:500;color:var(--ink);text-transform:uppercase}
.heading{position:absolute;font-size:27px;font-weight:700;color:var(--red);text-transform:uppercase;white-space:nowrap}
.bar{position:absolute;width:9px;background:var(--red)}
.lorem{position:absolute;font-size:11px;line-height:18px;color:var(--muted)}
.photo{position:absolute}
/* hero */
.brand{position:absolute;left:181px;top:20px;font-size:22px;font-weight:800;color:var(--red);text-transform:uppercase;letter-spacing:1px}
.ghost-word{position:absolute;left:172px;top:62px;font-size:118px;font-weight:800;color:#efefef;letter-spacing:6px;line-height:1}
.phone{position:absolute;left:557px;top:18px;display:flex;align-items:center;gap:12px;font-size:23px;font-weight:600;color:var(--ink)}
.menu-btn{position:absolute;left:962px;top:22px;width:56px;height:38px;background:var(--ink);clip-path:polygon(18% 0,100% 0,82% 100%,0 100%)}
.menu-btn span{position:absolute;left:18px;width:22px;height:2px;background:#fff}
.hero-kicker{position:absolute;left:172px;top:140px;font-size:26px;font-weight:600;color:var(--ink)}
.hero-title{position:absolute;left:172px;top:170px;font-size:36px;font-weight:700;color:var(--red)}
.hero-copy{position:absolute;left:177px;top:236px;width:320px;font-size:12.5px;line-height:23px;color:var(--text)}
.dots{position:absolute;left:169px;top:443px;display:flex;gap:6px}
.dots i{width:13px;height:13px;border-radius:50%;background:var(--ink)}
.dots i.on{background:var(--red)}
/* stats */
.stat{position:absolute;top:1005px}
.stat b{display:block;font-size:19px;font-weight:600;color:var(--red)}
.stat small{display:block;font-size:11px;color:var(--text);margin-top:2px}
/* services */
.service-icon{position:absolute;width:70px;height:66px}
.service-title{position:absolute;font-size:13px;font-weight:700;color:var(--ink)}
.service-copy{position:absolute;width:262px;font-size:10.5px;line-height:14px;color:var(--muted)}
/* tabs */
.tab{position:absolute;top:1915px;height:48px;display:flex;align-items:center;justify-content:center;font-size:10.5px;font-weight:700;color:var(--ink);text-transform:uppercase}
.tab svg{position:absolute;left:0;top:0}
.tab span{position:relative}
.check{position:absolute;left:542px;width:34px;height:34px}
.point-title{position:absolute;left:609px;font-size:11px;font-weight:700;color:var(--ink);text-transform:uppercase}
.point-copy{position:absolute;left:610px;width:320px;font-size:10.5px;line-height:14px;color:var(--muted)}
/* testimonial */
.quote-text{position:absolute;left:250px;top:2506px;width:275px;font-size:11px;line-height:19px;font-style:italic;font-weight:500;color:var(--text)}
.quote-name{position:absolute;left:255px;top:2607px;font-size:16px;font-weight:700;font-style:italic;color:var(--ink)}
.quote-place{position:absolute;left:254px;top:2628px;font-size:10px;font-style:italic;font-weight:500;color:var(--ink)}
.arrow-btn{position:absolute;top:2680px;width:46px;height:31px;background:var(--ink);clip-path:polygon(22% 0,100% 0,78% 100%,0 100%);display:flex;align-items:center;justify-content:center}
/* newsletter */
.newsletter{position:absolute;left:283px;top:2776px;width:638px;height:192px;background:var(--panel)}
.newsletter h2{position:absolute;left:77px;top:38px;font-size:26px;font-weight:700;color:var(--red);text-transform:uppercase}
.newsletter .field{position:absolute;left:135px;top:118px;font-size:19px;color:#6b6b70}
/* footer */
.foot-head{position:absolute;top:3096px;font-size:16px;font-weight:500;color:var(--red);text-transform:uppercase}
.foot-links{position:absolute;left:185px;top:3146px;list-style:none}
.foot-links li{font-size:11.5px;color:#fff;height:28.5px;display:flex;align-items:center;gap:9px}
.find-label{position:absolute;left:582px;font-size:10px;color:#9a9aa0}
.find-value{position:absolute;left:582px;font-size:11.5px;font-weight:600;color:#fff}
.foot-brand{position:absolute;left:778px;top:3084px;color:#fff;font-weight:800;text-transform:uppercase;line-height:1}
.copyright{position:absolute;left:784px;top:3178px;font-size:13px;color:#fff}
</style>
</head>
<body>
<div class="canvas">

  <!-- HERO -->
  <svg class="shape" width="1200" height="560" viewBox="0 0 1200 560">
    <polygon points="0,0 168,0 0,262" fill="var(--red)"/>
    <polygon points="168,0 176,0 0,275 0,262" fill="var(--ink)"/>
    <polygon points="797,0 1200,0 1200,498 590,498" fill="var(--red)"/>
    <polygon points="780,0 797,0 700,150 684,150" fill="var(--ink)"/>
  </svg>
  <div class="ghost-word" aria-hidden="true">VELTRA</div>
  <div class="brand">Veltra Auto Repair</div>
  <div class="phone">
    <svg width="26" height="26" viewBox="0 0 24 24" fill="none" stroke="var(--red)" stroke-width="1.6"><path d="M5 3h4l2 5-2.5 1.5a11 11 0 0 0 6 6L16 13l5 2v4a2 2 0 0 1-2 2A17 17 0 0 1 3 5a2 2 0 0 1 2-2z"/><path d="M15 3a6 6 0 0 1 6 6M15 7a2 2 0 0 1 2 2"/></svg>
    (209) 555-0142
  </div>
  <div class="btn" style="left:797px;top:22px;width:160px;height:38px;font-size:12px;letter-spacing:0.3px">BOOK APPOINTMENT</div>
  <div class="menu-btn"><span style="top:12px"></span><span style="top:18px"></span><span style="top:24px"></span></div>

  <div class="hero-kicker">WELCOME TO</div>
  <div class="hero-title">VELTRA AUTO REPAIR</div>
  <p class="hero-copy">Lorem ipsum dolor sit amet, consectetur adipiscing elit, sed do eiusmod tempor incididunt ut labore et dolore magna aliqua.</p>
  <div class="btn" style="left:175px;top:358px;width:138px;height:38px">EXPLORE&nbsp;&nbsp;›</div>
  <div class="dots"><i></i><i></i><i class="on"></i><i></i><i></i></div>
  <div class="photo" role="img" aria-label="Silver convertible sports car, front three-quarter view"
       style="left:482px;top:165px;width:718px;height:370px;border-radius:120px 0 60px 220px;background:linear-gradient(160deg,#e4e4e6 0%,#c4c5c8 55%,#8e9095 100%)"></div>

  <!-- BRAND STRIP -->
  <svg class="shape" style="top:587px" width="1200" height="80" viewBox="0 0 1200 80">
    <polygon points="0,0 85,0 62,80 0,80" fill="var(--ink)"/>
    <path d="M40 30l-9 10 9 10" fill="none" stroke="var(--red)" stroke-width="2.5"/>
    <g fill="#fff" stroke="#d4d4d6">
      <polygon points="98,0 258,0 240,80 78,80"/>
      <polygon points="272,0 432,0 414,80 252,80"/>
      <polygon points="446,0 606,0 588,80 426,80"/>
      <polygon points="620,0 780,0 762,80 600,80"/>
      <polygon points="794,0 954,0 936,80 774,80"/>
      <polygon points="968,0 1128,0 1110,80 948,80"/>
    </g>
    <polygon points="1140,0 1200,0 1200,80 1118,80" fill="var(--ink)"/>
    <path d="M1164 30l9 10-9 10" fill="none" stroke="var(--red)" stroke-width="2.5"/>
    <g font-family="Barlow, sans-serif" font-size="18" font-weight="600" fill="#3a3a3e" text-anchor="middle">
      <text x="168" y="46">Marlow</text>
      <text x="342" y="46">Quadrel</text>
      <text x="516" y="46">Toryn</text>
      <text x="690" y="46">Halden</text>
      <text x="864" y="46">Vessik</text>
      <text x="1038" y="46">Calloway</text>
    </g>
  </svg>

  <!-- ABOUT -->
  <svg class="shape" width="1200" height="1200" viewBox="0 0 1200 1200">
    <polygon points="171,728 581,728 531,1121 101,1121" fill="#fff" stroke="#8a8a8e" stroke-width="1.2"/>
    <defs><linearGradient id="garage" x1="0" y1="0" x2="1" y2="1"><stop offset="0" stop-color="#5d6a70"/><stop offset="1" stop-color="#1f2427"/></linearGradient></defs>
    <polygon points="180,740 566,740 520,1110 113,1110" fill="url(#garage)" role="img" aria-label="Mechanic working under a car raised on a lift in a workshop"/>
    <polygon points="386,969 583,969 544,1151 343,1151" fill="var(--red)"/>
    <text x="470" y="1043" text-anchor="middle" font-family="Barlow, sans-serif" font-size="54" font-weight="600" fill="#fff">100+</text>
    <text x="462" y="1082" text-anchor="middle" font-family="Barlow, sans-serif" font-size="22" fill="#fff">SERVICES</text>
    <text x="465" y="1111" text-anchor="middle" font-family="Barlow, sans-serif" font-size="22" fill="#fff">AVAILABLE</text>
  </svg>
  <div class="bar" style="left:656px;top:741px;height:42px"></div>
  <div class="kicker" style="left:683px;top:734px;font-size:14px">Who we are</div>
  <div class="heading" style="left:682px;top:752px;font-size:27px">Little bit about Veltra</div>
  <p class="lorem" style="left:655px;top:805px;width:355px">Lorem ipsum dolor sit amet, consectetur adipiscing elit, sed do eiusmod tempor incididunt ut labore et dolore magna aliqua. Lorem ipsum dolor sit amet, consectetur adipiscing elit, sed do eiusmod tempor incididunt ut labore et dolore magna aliqua.Lorem ipsum dolor sit amet, consectetur adipiscing elit, sed do eiusmod tempor incididunt ut labore et dolore magna aliqua.Lorem ipsum dolor sit amet.</p>
  <p class="lorem" style="left:655px;top:935px;width:360px">Lorem ipsum dolor sit amet, consectetur adipiscing elit, sed do eiusmod tempor incididunt ut labore et dolore magna aliqua.</p>
  <div class="stat" style="left:656px"><b>1000+</b><small>HAPPY CLIENTS</small></div>
  <div class="abs" style="left:758px;top:1008px;width:1px;height:36px;background:var(--line)"></div>
  <div class="stat" style="left:771px;top:1007px"><b>1000+</b><small>HAPPY CLIENTS</small></div>
  <div class="abs" style="left:868px;top:1008px;width:1px;height:36px;background:var(--line)"></div>
  <div class="stat" style="left:881px;top:1007px"><b>1000+</b><small>HAPPY CLIENTS</small></div>
  <div class="btn" style="left:658px;top:1112px;width:138px;height:39px">READ MORE</div>

  <!-- WHAT WE DO -->
  <svg class="shape" style="top:1244px" width="1200" height="520" viewBox="0 0 1200 520">
    <polygon points="0,0 90,0 0,150" fill="var(--ink)"/>
    <polygon points="90,0 103,0 0,175 0,150" fill="var(--red)"/>
    <polygon points="862,0 1200,0 1200,456 620,456" fill="var(--ink)"/>
    <polygon points="828,0 862,0 740,236 722,236" fill="var(--red)"/>
  </svg>
  <div class="bar" style="left:183px;top:1244px;height:45px"></div>
  <div class="kicker" style="left:206px;top:1242px;font-size:18px">What we do</div>
  <div class="heading" style="left:206px;top:1261px;font-size:26px">Maintenance, service, &amp; repair</div>

  <svg class="service-icon" style="left:181px;top:1338px" viewBox="0 0 70 66">
    <circle cx="30" cy="33" r="29" fill="var(--red-soft)"/>
    <g fill="none" stroke="var(--ink)" stroke-width="2"><circle cx="45" cy="40" r="8"/><circle cx="45" cy="40" r="3"/><path d="M34 14l10 12M56 12l-8 14M28 18l6-6 4 4-6 6zM52 8l6 4-2 4-6-4z"/></g>
  </svg>
  <div class="service-title" style="left:285px;top:1338px">ENGINE</div>
  <p class="service-copy" style="left:287px;top:1362px">Lorem ipsum dolor sit amet, consectetur adipiscing elit, sed do eiusmod tempor incididunt ut labore et dolore magna aliqua.</p>

  <svg class="service-icon" style="left:181px;top:1420px" viewBox="0 0 70 66">
    <circle cx="30" cy="33" r="29" fill="var(--red-soft)"/>
    <g fill="none" stroke="var(--ink)" stroke-width="2"><circle cx="42" cy="35" r="20"/><circle cx="42" cy="35" r="9"/><circle cx="42" cy="35" r="3"/><path d="M28 20a20 20 0 0 0 0 30"/></g>
  </svg>
  <div class="service-title" style="left:290px;top:1422px">BREAK DISC</div>
  <p class="service-copy" style="left:293px;top:1444px">Lorem ipsum dolor sit amet, consectetur adipiscing elit, sed do eiusmod tempor incididunt ut labore et dolore magna aliqua.</p>

  <svg class="service-icon" style="left:181px;top:1504px" viewBox="0 0 70 66">
    <circle cx="30" cy="33" r="29" fill="var(--red-soft)"/>
    <g fill="none" stroke="var(--ink)" stroke-width="2.4"><path d="M20 52a22 22 0 1 1 36 0"/><path d="M38 40l10-10"/><circle cx="38" cy="40" r="3" fill="var(--ink)"/><path d="M38 18v4M22 26l3 3M54 26l-3 3M18 40h4M58 40h-4"/></g>
  </svg>
  <div class="service-title" style="left:293px;top:1508px">SPEEDOMETER</div>
  <p class="service-copy" style="left:296px;top:1530px">Lorem ipsum dolor sit amet, consectetur adipiscing elit, sed do eiusmod tempor incididunt ut labore et dolore magna aliqua.</p>

  <svg class="service-icon" style="left:181px;top:1596px" viewBox="0 0 70 66">
    <circle cx="30" cy="33" r="29" fill="var(--red-soft)"/>
    <circle cx="46" cy="38" r="22" fill="var(--ink)"/>
    <circle cx="46" cy="38" r="14" fill="none" stroke="var(--red-soft)" stroke-width="2"/>
    <g stroke="var(--red-soft)" stroke-width="2.5"><path d="M46 24v28M32 38h28M36 28l20 20M56 28L36 48"/></g>
    <circle cx="46" cy="38" r="4" fill="var(--ink)" stroke="var(--red-soft)" stroke-width="2"/>
  </svg>
  <div class="service-title" style="left:290px;top:1600px">CAR WHEELS</div>
  <p class="service-copy" style="left:293px;top:1628px">Lorem ipsum dolor sit amet, consectetur adipiscing elit, sed do eiusmod tempor incididunt ut labore et dolore magna aliqua.</p>

  <div class="photo" role="img" aria-label="Cutaway render of a silver SUV showing engine and suspension"
       style="left:577px;top:1374px;width:550px;height:370px;border-radius:160px 80px 60px 200px;background:linear-gradient(150deg,#eeeeef 0%,#bfc1c4 60%,#8b8d92 100%)"></div>
  <div class="btn" style="left:184px;top:1720px;width:140px;height:40px">READ MORE</div>

  <!-- WHY CHOOSE US -->
  <svg class="shape" style="top:2030px" width="600" height="230" viewBox="0 0 600 230">
    <polygon points="492,5 514,5 432,225 400,225" fill="var(--red)"/>
    <polygon points="470,40 492,5 410,225 392,225" fill="var(--ink)"/>
  </svg>
  <div class="photo" role="img" aria-label="Smiling mechanic in blue overalls holding a wrench"
       style="left:188px;top:1834px;width:272px;height:421px;border-radius:110px 110px 10px 10px;background:linear-gradient(180deg,#c7a48a 0%,#2d6bc0 35%,#1f4f99 100%)"></div>
  <div class="bar" style="left:540px;top:1831px;height:45px"></div>
  <div class="kicker" style="left:565px;top:1828px;font-size:18px">Our universe selling point</div>
  <div class="heading" style="left:565px;top:1850px;font-size:26px">Why choose us</div>

  <div class="tab" style="left:540px;width:156px;color:#fff">
    <svg width="156" height="48"><polygon points="12,1 155,1 144,47 1,47" fill="var(--red)" stroke="var(--red)"/></svg><span>Our advantages</span></div>
  <div class="tab" style="left:692px;width:154px">
    <svg width="154" height="48"><polygon points="12,1 153,1 142,47 1,47" fill="#fff" stroke="var(--ink)"/></svg><span>Additional services</span></div>
  <div class="tab" style="left:842px;width:154px">
    <svg width="154" height="48"><polygon points="12,1 153,1 142,47 1,47" fill="#fff" stroke="var(--ink)"/></svg><span>About performance</span></div>

  <svg class="check" style="top:2018px" viewBox="0 0 34 34"><rect x="1" y="1" width="32" height="32" fill="none" stroke="var(--red-soft)" stroke-width="1.5"/><path d="M11 17l5 5 8-10" fill="none" stroke="var(--red-soft)" stroke-width="1.5"/></svg>
  <div class="point-title" style="top:2010px">We make it easy</div>
  <p class="point-copy" style="top:2030px">Lorem ipsum dolor sit amet, consectetur adipiscing elit, sed do eiusmod tempor incididunt ut labore et dolore magna aliqua.</p>

  <svg class="check" style="top:2086px" viewBox="0 0 34 34"><rect x="1" y="1" width="32" height="32" fill="none" stroke="var(--red-soft)" stroke-width="1.5"/><path d="M11 17l5 5 8-10" fill="none" stroke="var(--red-soft)" stroke-width="1.5"/></svg>
  <div class="point-title" style="top:2082px">Fair and transparent pricing</div>
  <p class="point-copy" style="top:2102px">Lorem ipsum dolor sit amet, consectetur adipiscing elit, sed do eiusmod tempor incididunt ut labore et dolore magna aliqua.</p>

  <svg class="check" style="top:2152px" viewBox="0 0 34 34"><rect x="1" y="1" width="32" height="32" fill="none" stroke="var(--red-soft)" stroke-width="1.5"/><path d="M11 17l5 5 8-10" fill="none" stroke="var(--red-soft)" stroke-width="1.5"/></svg>
  <div class="point-title" style="top:2148px">Satisfaction guaranteed</div>
  <p class="point-copy" style="top:2169px">Lorem ipsum dolor sit amet, consectetur adipiscing elit, sed do eiusmod tempor incididunt ut labore et dolore magna aliqua.</p>

  <svg class="check" style="top:2224px" viewBox="0 0 34 34"><rect x="1" y="1" width="32" height="32" fill="none" stroke="var(--red-soft)" stroke-width="1.5"/><path d="M11 17l5 5 8-10" fill="none" stroke="var(--red-soft)" stroke-width="1.5"/></svg>
  <div class="point-title" style="top:2220px">OEM factory parts warranty</div>
  <p class="point-copy" style="top:2241px">Lorem ipsum dolor sit amet, consectetur adipiscing elit, sed do eiusmod tempor incididunt ut labore et dolore magna aliqua.</p>

  <!-- TESTIMONIALS -->
  <div class="bar" style="left:235px;top:2361px;height:43px"></div>
  <div class="kicker" style="left:261px;top:2357px;font-size:15px">Testimonials</div>
  <div class="heading" style="left:260px;top:2376px;font-size:27px">Our happy clients</div>
  <svg class="shape" width="1200" height="2720" viewBox="0 0 1200 2720" style="pointer-events:none">
    <polygon points="240,2447 591,2447 537,2646 185,2646" fill="#fff" stroke="#8a8a8e" stroke-width="1.2"/>
    <path d="M254 2470c0-12 8-20 18-22v6c-5 2-8 6-8 10 6 0 10 4 10 9s-4 10-10 10-10-5-10-13zm28 0c0-12 8-20 18-22v6c-5 2-8 6-8 10 6 0 10 4 10 9s-4 10-10 10-10-5-10-13z" fill="var(--ink)"/>
    <polygon points="664,2363 1013,2363 946,2703 595,2703" fill="#fff" stroke="#8a8a8e" stroke-width="1.2"/>
    <defs><linearGradient id="drive" x1="0" y1="0" x2="1" y2="0.6"><stop offset="0" stop-color="#3c4a5a"/><stop offset="0.6" stop-color="#8a7a66"/><stop offset="1" stop-color="#e8a95a"/></linearGradient></defs>
    <polygon points="672,2373 1000,2373 936,2693 606,2693" fill="url(#drive)" role="img" aria-label="Happy couple sitting in the front seats of a car at sunset"/>
  </svg>
  <p class="quote-text">Lorem ipsum dolor sit amet, consectetur adipiscing elit, sed do eiusmod tempor incididunt ut labore et dolore magna aliqua. Lorem ipsum dolor sit amet, consectetur adipiscing elit, sed do eiusmod .</p>
  <div class="quote-name">Dana Whitlow</div>
  <div class="quote-place">California</div>
  <div class="arrow-btn" style="left:209px"><svg width="10" height="12"><path d="M7 1L2 6l5 5" fill="none" stroke="#fff" stroke-width="1.8"/></svg></div>
  <div class="arrow-btn" style="left:257px"><svg width="10" height="12"><path d="M3 1l5 5-5 5" fill="none" stroke="#fff" stroke-width="1.8"/></svg></div>

  <!-- NEWSLETTER -->
  <section class="newsletter">
    <h2>Subscribe our newsletter</h2>
    <svg class="abs" style="left:70px;top:113px" width="52" height="36" viewBox="0 0 52 36">
      <rect x="12" y="3" width="37" height="29" fill="none" stroke="var(--ink)" stroke-width="3"/>
      <path d="M12 4l18 15 19-15" fill="none" stroke="var(--ink)" stroke-width="3"/>
      <path d="M0 16h9M3 22h6M0 28h9" stroke="var(--red)" stroke-width="3"/>
    </svg>
    <div class="field">Type your Email</div>
    <div class="btn" style="left:404px;top:104px;width:160px;height:54px;font-weight:500;font-size:16px;letter-spacing:0.3px">SUBSCRIBE</div>
  </section>

  <!-- FOOTER -->
  <svg class="shape" style="top:3020px" width="1200" height="319" viewBox="0 0 1200 319">
    <polygon points="0,23 1200,3 1200,319 0,319" fill="var(--ink)"/>
    <polygon points="0,23 1200,3 1200,16 0,30" fill="var(--red)"/>
  </svg>
  <div class="foot-head" style="left:185px">Quick links</div>
  <ul class="foot-links">
    <li>› <span>Home</span></li>
    <li>› <span>About</span></li>
    <li>› <span>services</span></li>
    <li>› <span>Blogs</span></li>
    <li>› <span>Contact</span></li>
  </ul>
  <div class="foot-head" style="left:345px">Follow us</div>
  <svg class="abs" style="left:343px;top:3148px" width="106" height="28" viewBox="0 0 106 28">
    <circle cx="14" cy="14" r="13" fill="none" stroke="#4a4a50"/><circle cx="14" cy="14" r="6" fill="#3a64c8"/>
    <circle cx="52" cy="14" r="13" fill="none" stroke="#4a4a50"/><circle cx="52" cy="14" r="6" fill="#3a9ae0"/>
    <circle cx="90" cy="14" r="13" fill="none" stroke="#4a4a50"/><circle cx="90" cy="14" r="6" fill="var(--red)"/>
  </svg>
  <div class="foot-head" style="left:544px">Find us</div>
  <svg class="abs" style="left:544px;top:3148px" width="28" height="132" viewBox="0 0 28 132">
    <g fill="none" stroke="var(--red)" stroke-width="1.3">
      <circle cx="14" cy="13" r="12"/><path d="M14 19s-5-5-5-8a5 5 0 0 1 10 0c0 3-5 8-5 8z"/><circle cx="14" cy="11" r="1.6"/>
      <circle cx="14" cy="58" r="12"/><path d="M9 52h3l1.5 3-1.5 1a6 6 0 0 0 3 3l1-1.5 3 1.5v3a1 1 0 0 1-1 1A9 9 0 0 1 8 53a1 1 0 0 1 1-1z"/>
      <circle cx="14" cy="106" r="12"/><rect x="8" y="101" width="12" height="9"/><path d="M8 101l6 5 6-5"/>
    </g>
  </svg>
  <div class="find-label" style="top:3145px">Location</div>
  <div class="find-value" style="top:3160px">Location Goes Here</div>
  <div class="find-label" style="top:3190px">Phone No.</div>
  <div class="find-value" style="top:3206px">(209) 555-0142</div>
  <div class="find-label" style="top:3238px">Email</div>
  <div class="find-value" style="top:3254px">info@veltra.example</div>
  <div class="foot-brand"><div style="font-size:44px;letter-spacing:3px">Veltra</div><div style="font-size:20px;margin-top:2px;padding-left:104px">Auto Repair</div></div>
  <div class="copyright">© 2023 Veltra,&nbsp; All rights reserved.</div>
  <div class="btn red" style="left:780px;top:3229px;width:195px;height:49px">BOOK APPOINTMENT</div>

</div>
</body>
</html>
```